Quorvex business card design

create modern and tech looking business card that is clean but effectively communciates that we are a cloud communications company.
Should have at minimum:
Employee Name
Postion
Phone Number
Email
website
create modern and tech looking business card that is clean but effectively communciates that we are a cloud communications company. We have two logo color schemes (attached) so would like to see designs both ways
Should have at minimum:
Employee Name
Postion
Phone Number
Email
website

```html
<!DOCTYPE html>
<html lang="en">
<head>
<meta charset="UTF-8">
<title>Quorvex Business Card</title>
<link href="https://fonts.googleapis.com/css2?family=Roboto:wght@400;500;700&display=swap" rel="stylesheet">
<style>
  :root {
    --backdrop: #b9b9b9;
    --card: #efefef;
    --ink: #4a4a4a;
    --teal: #2aa9c9;
    --purple: #5a2a84;
    --white: #ffffff;
  }
  * { margin: 0; padding: 0; box-sizing: border-box; }
  html, body {
    width: 1200px;
    height: 576px;
    overflow: hidden;
    background: var(--backdrop);
    font-family: "Roboto", Arial, sans-serif;
  }
  .canvas {
    position: relative;
    width: 1200px;
    height: 576px;
  }
  .card {
    position: absolute;
    top: 139px;
    background: var(--card);
    border-radius: 14px;
    overflow: hidden;
    box-shadow: 0 3px 6px rgba(0,0,0,0.25);
  }
  .card-front { left: 82px; width: 485px; height: 293px; }
  .card-back { left: 602px; width: 480px; height: 289px; }

  .wordmark {
    position: absolute;
    display: flex;
    align-items: center;
    gap: 12px;
    color: var(--ink);
    font-weight: 500;
    letter-spacing: 2px;
  }
  .wordmark-mark {
    background: var(--purple);
    flex: none;
  }
  .card-front .wordmark {
    left: 50%;
    top: 50%;
    transform: translate(-50%, -50%);
    font-size: 36px;
  }
  .card-front .wordmark-mark { width: 34px; height: 34px; }
  .card-back .wordmark {
    left: 30px;
    top: 124px;
    font-size: 24px;
    gap: 9px;
  }
  .card-back .wordmark-mark { width: 24px; height: 24px; }

  .contact {
    position: absolute;
    left: 265px;
    top: 92px;
    color: var(--ink);
  }
  .contact-name {
    font-size: 22px;
    font-weight: 500;
    color: var(--teal);
    line-height: 1;
  }
  .contact-role {
    font-size: 12px;
    margin-top: 8px;
  }
  .contact-list {
    list-style: none;
    margin-top: 14px;
    font-size: 13px;
  }
  .contact-list li {
    display: flex;
    align-items: center;
    gap: 9px;
    height: 18px;
  }
  .contact-list svg { width: 11px; height: 11px; fill: var(--teal); flex: none; }

  .footer-bands {
    position: absolute;
    left: 0;
    bottom: 0;
    width: 480px;
    height: 30px;
  }
  .footer-web {
    position: absolute;
    left: 265px;
    bottom: 10px;
    font-size: 12px;
    color: var(--white);
  }
</style>
</head>
<body>
<div class="canvas">
  <section class="card card-front">
    <div class="wordmark"><span class="wordmark-mark"></span>QUORVEX</div>
  </section>

  <section class="card card-back">
    <div class="wordmark"><span class="wordmark-mark"></span>QUORVEX</div>

    <div class="contact">
      <h1 class="contact-name">Daniel Reyes</h1>
      <p class="contact-role">Managing Director</p>
      <ul class="contact-list">
        <li>
          <svg viewBox="0 0 12 12" aria-hidden="true"><path d="M2.5 1 L4.5 1 L5 3.5 L3.8 4.4 A7 7 0 0 0 7.6 8.2 L8.5 7 L11 7.5 L11 9.5 A1.5 1.5 0 0 1 9.5 11 A8.5 8.5 0 0 1 1 2.5 A1.5 1.5 0 0 1 2.5 1 Z"/></svg>
          1800-555-0142
        </li>
        <li>
          <svg viewBox="0 0 12 12" aria-hidden="true"><path d="M0.5 2.5 H11.5 V9.5 H0.5 Z M1.3 3.2 L6 6.6 L10.7 3.2 Z"/></svg>
          dreyes@quorvexcloud.com
        </li>
      </ul>
    </div>

    <svg class="footer-bands" viewBox="0 0 480 30" aria-hidden="true">
      <rect x="0" y="18" width="480" height="12" fill="var(--teal)"/>
      <polygon points="230,0 480,0 480,30 212,30" fill="var(--purple)"/>
    </svg>
    <p class="footer-web">www.quorvexcloud.com</p>
  </section>
</div>
</body>
</html>
```